Home Remodeling company needs a business card design

we need a business card design for home remodeling company in hamilton county, indiana USA. we offers a wide range of construction services including whole house renovations, Design and Build Basements and Kitchen and Bathroom Remodeling . we would like to see designs for both site of business card that use the same color of the company logo and also including all information below :
1- Samir Daoudi CEO / General Contractor
2- all company contacts Telephone numbers ( 1-888-TOVAL-42 ) ( 317-555-0192) email address ( info@tovalhome.example) website ( www.tovalhome.example ) and social media logos (Facebook- twitter- google plus )
3- company logo
4- licensed . insured . bonded

```html
<!DOCTYPE html>
<html lang="en">
<head>
<meta charset="utf-8">
<title>Toval Home Remodeling – Business Card</title>
<link href="https://fonts.googleapis.com/css2?family=Open+Sans:ital,wght@0,400;0,600;1,400&display=swap" rel="stylesheet">
<style>
  :root {
    --stage: #e6e3df;
    --card: #1b1b1c;
    --card-edge: #232324;
    --white: #f4f4f4;
    --grey: #a9a9a9;
    --rule: #5a5a5a;
    --red: #c8202a;
  }
  * { margin: 0; padding: 0; box-sizing: border-box; }
  html, body {
    width: 1200px; height: 787px; overflow: hidden;
    background: var(--stage);
    font-family: "Open Sans", Arial, sans-serif;
  }
  .stage {
    width: 1200px; height: 787px;
    display: flex; align-items: center; justify-content: center; gap: 40px;
  }
  .card {
    position: relative;
    width: 540px; height: 309px;
    background: var(--card);
    border: 1px solid var(--card-edge);
    box-shadow: 0 10px 28px rgba(0,0,0,.25);
    color: var(--white);
  }

  /* company name placeholder */
  .company-name {
    font-weight: 600; line-height: 1.1;
    color: var(--white);
  }

  /* front side */
  .card--front { display: flex; flex-direction: column; align-items: center; justify-content: center; }
  .card--front .company-name { font-size: 48px; }
  .credentials {
    margin-top: 24px;
    font-size: 15px; font-style: italic; color: var(--white); letter-spacing: .3px;
  }
  .social { display: flex; gap: 8px; margin-top: 14px; }
  .social__dot { width: 18px; height: 18px; border-radius: 50%; background: var(--white); }
  .front-rule {
    margin-top: 10px; width: 180px; height: 1px;
    background: linear-gradient(90deg, transparent, var(--rule), transparent);
  }

  /* back side */
  .card--back { display: flex; align-items: center; padding: 0 28px 0 40px; }
  .card--back .company-name { font-size: 44px; width: 180px; text-align: center; }
  .divider {
    width: 1px; height: 170px; margin: 0 24px 0 26px;
    background: linear-gradient(180deg, transparent, var(--grey), transparent);
  }
  .contact__name { color: var(--red); font-weight: 600; font-size: 19px; line-height: 1.2; }
  .contact__title { font-size: 14px; color: var(--white); margin-bottom: 8px; }
  .contact__list { list-style: none; }
  .contact__item { display: flex; align-items: center; gap: 10px; font-size: 14.5px; line-height: 1.55; white-space: nowrap; }
  .contact__icon { width: 14px; height: 14px; flex: none; fill: var(--red); }
</style>
</head>
<body>
<main class="stage">

  <section class="card card--front" aria-label="Card front">
    <p class="company-name">Toval</p>
    <p class="credentials">licensed | insured | bonded</p>
    <div class="social" aria-label="Social media">
      <span class="social__dot"></span>
      <span class="social__dot"></span>
      <span class="social__dot"></span>
    </div>
    <div class="front-rule"></div>
  </section>

  <section class="card card--back" aria-label="Card back">
    <p class="company-name">Toval</p>
    <div class="divider"></div>
    <div class="contact">
      <p class="contact__name">Samir Daoudi</p>
      <p class="contact__title">CEO / General Contractor</p>
      <ul class="contact__list">
        <li class="contact__item">
          <svg class="contact__icon" viewBox="0 0 16 16" aria-hidden="true"><path d="M1 5c0-2 3-3.5 7-3.5S15 3 15 5l-3 1.2-.8-2H4.8l-.8 2zM4 7h8l2 7H2z"/><circle cx="8" cy="10.5" r="1.8" fill="#1b1b1c"/></svg>
          <span>1-888-TOVAL-42</span>
        </li>
        <li class="contact__item">
          <svg class="contact__icon" viewBox="0 0 16 16" aria-hidden="true"><path d="M4 0h8a1 1 0 0 1 1 1v14a1 1 0 0 1-1 1H4a1 1 0 0 1-1-1V1a1 1 0 0 1 1-1zm1 2v10h6V2z"/><circle cx="8" cy="14" r=".9" fill="#1b1b1c"/></svg>
          <span>317-555-0192</span>
        </li>
        <li class="contact__item">
          <svg class="contact__icon" viewBox="0 0 16 16" aria-hidden="true"><path d="M0 3h16v1.5L8 9.5 0 4.5zM0 6.3l8 5 8-5V13H0z"/></svg>
          <span>info@tovalhome.example</span>
        </li>
        <li class="contact__item">
          <svg class="contact__icon" viewBox="0 0 16 16" aria-hidden="true"><circle cx="8" cy="8" r="7.5"/><path d="M.5 8h15M8 .5c-3 3.5-3 11.5 0 15M8 .5c3 3.5 3 11.5 0 15" stroke="#1b1b1c" stroke-width="1" fill="none"/></svg>
          <span>www.tovalhome.example</span>
        </li>
      </ul>
    </div>
  </section>

</main>
</body>
</html>
```